Luxury Skincare Product Box Packaging Design

Vorastelle is a range of skincare products that help protect, nourish, and strengthen even the most sensitive skin, ensuring it is healthy, glowing, calm, and soft. Skincare practices support skin to enhance its appearance and relieve skin conditions. Your skin reflects your health. It is your body canvas and is an asset. The products contain naturally derived ingredients, aromatherapy oils, sustainable and ethical ingredients, organic ingredients where possible, natural preservatives and Australian oils, fruits, and extracts.

Vorastelle
Tagline is "Where Calm Finds Bloom"

Our products do not contain sulphates, parabens, phthalates, petrochemicals, synthetic colours, nor synthetic fragrances.

Everything about the Vorastelle Skincare name is creative and communicates luxury. Vorastelle from your first glance of the name, you will know that this is a company with excellent products.

By keeping it simple, unique, and elegant is often associated with high quality and is a way to establish trust. Vorastelle is a product that is “pure” and natural, so Vorastelle packaging would look simple, elegant, and clean.

I have uploaded the actual logo design and individual labels for the current skincare range I currently with the ingredients included so you can get an understanding of what I like. I have also added samples of package designs I quite like to assist with your designs.

Each Product box packaging sizes are as follows:

Product One - Exfoliating Herbs: 110mm (H) x 33mm Diameter
Product Two - Probiotic Lotion: 138mm (H) x 33mm Diameter
Product Three - Vitamin A Serum: 120mm (H) x 30mm Diameter
Updates

The Measurements are as follows: Product One: 110mm (H) x 33mm Diameter Product Two: 138mm (H) x 33mm Diameter Product Three: 120mm (H) x 30mm Diameter

Target Market(s)

Women

Requirements
Must have
• Logo, Product Name and ingredients and if you can barcode on the packaging that is the box design I am after
Nice to have
• samples of designs I like but open to suggestions

```html
<!DOCTYPE html>
<html lang="en">
<head>
<meta charset="utf-8">
<title>Vorastelle – Gentle Exfoliating Herbs Box Dieline</title>
<link href="https://fonts.googleapis.com/css2?family=DM+Serif+Text&family=Lato:wght@400;700&display=swap" rel="stylesheet">
<style>
  :root {
    --backdrop: #e0dfdd;
    --board: #ffffff;
    --cut-line: #d9163c;
    --fold-line: #1ab0e8;
    --sage-band: #bddbcb;
    --ink: #1d1d1d;
    --rose-gold: #c08f78;
  }
  html, body {
    margin: 0;
    padding: 0;
    width: 761px;
    height: 1200px;
    overflow: hidden;
    background: var(--backdrop);
  }
  .canvas {
    width: 761px;
    height: 1200px;
    display: flex;
    align-items: center;
    justify-content: center;
  }
  .dieline { width: 741px; height: 941px; display: block; }
  .bleed { fill: var(--board); stroke: var(--board); stroke-width: 30; stroke-linejoin: round; }
  .cut { fill: var(--board); stroke: var(--cut-line); stroke-width: 3; stroke-linejoin: round; }
  .fold { stroke: var(--fold-line); stroke-width: 2.5; stroke-dasharray: 10 6; fill: none; }
  .band { fill: var(--sage-band); }
  .sans { font-family: "Lato", Arial, sans-serif; fill: var(--ink); }
  .serif { font-family: "DM Serif Text", Georgia, serif; fill: var(--ink); }
  .tagline { font-size: 14px; letter-spacing: 5px; }
  .brand-name { font-family: "Lato", Arial, sans-serif; font-size: 50px; font-weight: 400; fill: var(--rose-gold); letter-spacing: 4px; }
  .product-title { font-size: 25px; }
  .band-text { font-size: 16px; }
  .web { font-size: 12px; }
  .volume { font-size: 16px; }
  .back-title { font-size: 15px; font-weight: 700; }
  .back-copy { font-size: 11.5px; }
  .icon-label { font-size: 7.5px; }
  .icon-line { fill: none; stroke: var(--rose-gold); stroke-width: 1.5; }
  .icon-fill { fill: var(--rose-gold); opacity: 0.45; }
  .care-box { fill: none; stroke: var(--ink); stroke-width: 1.5; stroke-dasharray: 4 3; }
</style>
</head>
<body>
<main class="canvas">
<svg class="dieline" viewBox="290 1100 1000 1270" xmlns="http://www.w3.org/2000/svg" aria-label="Vorastelle Gentle Exfoliating Herbs carton dieline">
  <defs>
    <path id="carton-outline" d="
      M312 1416 L312 1400 L334 1388 L334 1293 L450 1293 Q462 1296 466 1306 L500 1416
      L744 1416 L778 1306 Q782 1296 794 1293 L908 1293 L908 1388 L932 1400
      L932 1228 A122 118 0 0 1 1177 1228 L1177 1416
      L1262 1430 L1262 2027 L1177 2041
      L932 2041 L932 2058 L918 2068 L897 2160 Q893 2170 882 2170 L768 2170 L768 2064 L744 2041
      L744 2230 A122 113 0 0 1 500 2230 L500 2041
      L476 2064 L476 2170 L360 2170 Q349 2170 345 2160 L323 2068 L312 2058 Z"/>
  </defs>

  <use href="#carton-outline" class="bleed"/>
  <use href="#carton-outline" class="cut"/>

  <!-- tuck notches -->
  <path d="M932 1228 L966 1228 L966 1240 M1177 1228 L1143 1228 L1143 1240" stroke="var(--cut-line)" stroke-width="3" fill="none"/>
  <path d="M500 2230 L534 2230 L534 2218 M744 2230 L710 2230 L710 2218" stroke="var(--cut-line)" stroke-width="3" fill="none"/>

  <!-- sage band -->
  <rect class="band" x="312" y="1948" width="865" height="26"/>

  <!-- fold lines -->
  <g class="fold">
    <line x1="312" y1="1416" x2="1177" y2="1416"/>
    <line x1="312" y1="2041" x2="1177" y2="2041"/>
    <line x1="500" y1="1416" x2="500" y2="2230"/>
    <line x1="744" y1="1416" x2="744" y2="2230"/>
    <line x1="932" y1="1228" x2="932" y2="2041"/>
    <line x1="1177" y1="1228" x2="1177" y2="2041"/>
    <line x1="966" y1="1240" x2="1143" y2="1240"/>
    <line x1="534" y1="2218" x2="710" y2="2218"/>
  </g>

  <!-- side panel: tagline -->
  <g class="side-panel">
    <text class="sans tagline" x="407" y="1682" text-anchor="middle" transform="rotate(-90 407 1682)">Where Calm Finds Bloom</text>
    <text class="sans web" x="408" y="1966" text-anchor="middle">www.vorastelle.com</text>
  </g>

  <!-- front panel -->
  <g class="front-panel">
    <text class="brand-name" x="622" y="1660" text-anchor="middle" transform="rotate(-72 622 1660)">Vorastelle</text>
    <text class="serif product-title" x="622" y="1876" text-anchor="middle">Gentle</text>
    <text class="serif product-title" x="622" y="1907" text-anchor="middle">Exfoliating Herbs</text>
    <text class="sans band-text" x="622" y="1967" text-anchor="middle">All Skin Types</text>
    <text class="sans volume" x="622" y="2007" text-anchor="middle">40 ml</text>
  </g>

  <!-- side panel: values icons -->
  <g class="icon-column">
    <circle class="icon-fill" cx="839" cy="1552" r="10" role="img" aria-label="Australian made koala icon"/>
    <text class="sans icon-label" x="839" y="1575" text-anchor="middle">Australian</text>
    <text class="sans icon-label" x="839" y="1584" text-anchor="middle">made</text>

    <path class="icon-line" d="M839 1622 L828 1611 A6 6 0 0 1 839 1603 A6 6 0 0 1 850 1611 Z"/>
    <text class="sans icon-label" x="839" y="1633" text-anchor="middle">100%</text>
    <text class="sans icon-label" x="839" y="1642" text-anchor="middle">Vegan</text>

    <circle class="icon-fill" cx="839" cy="1669" r="9" role="img" aria-label="Cruelty free rabbit icon"/>
    <text class="sans icon-label" x="839" y="1692" text-anchor="middle">Cruelty</text>
    <text class="sans icon-label" x="839" y="1701" text-anchor="middle">Free</text>

    <path class="icon-line" d="M839 1718 L849 1736 L829 1736 Z"/>
    <text class="sans icon-label" x="839" y="1749" text-anchor="middle">Please</text>
    <text class="sans icon-label" x="839" y="1758" text-anchor="middle">Recycle</text>

    <rect class="icon-line" x="830" y="1778" width="18" height="15" rx="2"/>
    <line class="icon-line" x1="828" y1="1778" x2="850" y2="1778"/>
    <text class="sans icon-label" x="839" y="1806" text-anchor="middle">6 months</text>
    <text class="sans icon-label" x="839" y="1815" text-anchor="middle">once open</text>

    <text class="sans web" x="838" y="1966" text-anchor="middle">www.vorastelle.com</text>
  </g>

  <!-- back panel -->
  <g class="back-panel" text-anchor="middle">
    <text class="serif back-title" x="1055" y="1464">Gentle Exfoliating Herbs</text>
    <g class="sans back-copy">
      <text x="1055" y="1502">· All Skin Types ·</text>
      <text x="1055" y="1516">Particularly beneficial for Sensitive,</text>
      <text x="1055" y="1530">stressed and delicate skins.</text>
      <text x="1055" y="1550">• • •</text>
      <text x="1055" y="1574">DIRECTIONS:</text>
      <text x="1055" y="1588">Mix a small amount with your favourite</text>
      <text x="1055" y="1602">cleanser. Massage into your face for</text>
      <text x="1055" y="1616">approximately one minute before</text>
      <text x="1055" y="1630">removing with water or a face cloth.</text>
      <text x="1055" y="1644">Use twice weekly.</text>
      <text x="1055" y="1656">• • •</text>
      <text x="1055" y="1674">INGREDIENTS:</text>
      <text x="1055" y="1688">ORYZA SATIVA (RICE) POWDER*,</text>
      <text x="1055" y="1702">ROSA GALLICA (ROSE PETALS)*,</text>
      <text x="1055" y="1716">JASMINUM OFFICINALE (JASMINE)</text>
      <text x="1055" y="1730">FLOWER, MATRICARIA RECUTITA</text>
      <text x="1055" y="1744">(CHAMOMILE FLOWERS)*, CAMELLIA</text>
      <text x="1055" y="1758">SINENSIS LEAF (GREEN TEA), LUFFA</text>
      <text x="1055" y="1772">CYLINDRICA FRUIT POWDER,</text>
      <text x="1055" y="1786">CALENDULA OFFICINALIS</text>
      <text x="1055" y="1800">(MARIGOLD FLOWERS)</text>
      <text x="1055" y="1814">*ORGANIC INGREDIENTS</text>
      <text x="1055" y="1840">• • •</text>
    </g>
    <rect class="care-box" x="947" y="1861" width="213" height="70"/>
    <g class="sans back-copy">
      <text x="1055" y="1878">Store in a cool dry place.</text>
      <text x="1055" y="1892">Caution For external use only.</text>
      <text x="1055" y="1906">Avoid contact with eyes.</text>
      <text x="1055" y="1920">If irritation occurs, discontinue use.</text>
    </g>
    <text class="sans volume" x="1055" y="2007">40 ml</text>
  </g>
</svg>
</main>
</body>
</html>
```